Gulf Book About Father - need cover design named - النور

The book talks about the good father who teaches his sons high principles and values, to be successful people in their lives.

Book size - 15 cm high
21 cm width
Data on the cover:
Name of the Book: النور
Author: دكتور/ مازن بن خليل القرطوني- Just write the name without the word writer
1440-2018
Logo of the Publishing House

Target Market(s)

Book submitted to children - Families - Schools - Public libraries

Requirements
Must have
• Design must include one or all of these options:
• The first option: a picture that has a meaning for a father who has values and principles with the son or children, expresses the contradiction - education, etc. -
• The background is to express the tender love or taken from the Emirates flag
• The second option: abstract art - with a background taken from the colors of the flag of the Emirates - or colors about love and tenderness
Should not have
• direct image

```html
<!DOCTYPE html>
<html lang="ar" dir="rtl">
<head>
<meta charset="utf-8">
<title>النور</title>
<link href="https://fonts.googleapis.com/css2?family=Cairo:wght@500;700&family=Lalezar&display=swap" rel="stylesheet">
<style>
  :root {
    --page: #fdfaf0;
    --violet-deep: #3f2f8f;
    --violet: #552a8c;
    --band: #6e2a8a;
    --ring: #5e2c92;
    --sun-top: #fde58a;
    --sun-mid: #fbe2b0;
    --sun-low: #f06a9a;
    --sun-ground: #e8386a;
    --gold: #ffd23a;
    --cream: #f7e6a8;
  }
  html, body {
    margin: 0;
    width: 1200px;
    height: 1200px;
    overflow: hidden;
    background: var(--page);
  }
  .cover {
    position: absolute;
    left: 50px;
    top: 207px;
    width: 1100px;
    height: 786px;
    background: radial-gradient(ellipse at 60% 45%, var(--violet-deep) 0%, var(--violet) 90%);
    overflow: hidden;
  }
  .band {
    position: absolute;
    left: 0;
    right: 0;
    background: linear-gradient(90deg, rgba(110,42,138,.55), rgba(140,40,140,.65));
  }
  .band--top { top: 40px; height: 34px; }
  .band--bottom { top: 683px; height: 72px; background: rgba(120,40,140,.35); }
  .sun-ring {
    position: absolute;
    left: 270px;
    top: 70px;
    width: 556px;
    height: 556px;
    border-radius: 50%;
    background: var(--ring);
  }
  .sun-photo {
    position: absolute;
    left: 286px;
    top: 86px;
    width: 524px;
    height: 524px;
    border-radius: 50%;
    background: linear-gradient(180deg, var(--sun-top) 0%, var(--sun-mid) 60%, var(--sun-low) 76%, var(--sun-ground) 100%);
  }
  .title {
    position: absolute;
    left: 0;
    right: 0;
    top: 425px;
    margin: 0;
    text-align: center;
    font-family: "Lalezar", "Cairo", sans-serif;
    font-size: 190px;
    line-height: 1;
    color: var(--gold);
    text-shadow: 0 0 18px rgba(255,120,200,.9), 0 0 4px rgba(255,255,255,.6);
  }
  .author, .date {
    position: absolute;
    left: 0;
    right: 0;
    text-align: center;
    font-family: "Cairo", sans-serif;
    color: var(--cream);
    margin: 0;
  }
  .author { top: 682px; font-size: 24px; font-weight: 700; }
  .date { top: 722px; font-size: 24px; font-weight: 500; letter-spacing: 2px; }
  .publisher {
    position: absolute;
    left: 985px;
    top: 688px;
    width: 70px;
    height: 62px;
    background: #fff;
    display: flex;
    flex-direction: column;
    align-items: center;
    justify-content: center;
    gap: 4px;
    font-family: "Cairo", sans-serif;
    font-weight: 700;
    font-size: 11px;
    color: #5a3a1a;
  }
  .publisher__mark { width: 18px; height: 18px; background: #5a3a1a; }
</style>
</head>
<body>
  <main class="cover">
    <div class="band band--top"></div>
    <div class="band band--bottom"></div>
    <div class="sun-ring"></div>
    <div class="sun-photo" role="img" aria-label="صورة أب يمسك بيد ابنه وهما يمشيان في الصحراء أمام شمس صفراء"></div>
    <h1 class="title">النور</h1>
    <p class="author">دكتور/ مازن بن خليل القرطوني</p>
    <p class="date">١٤٤٠-٢٠١٨</p>
    <div class="publisher">
      <span class="publisher__mark"></span>
      <span class="publisher__name">دار الضياء</span>
    </div>
  </main>
</body>
</html>
```